Energieberater sucht Flyer-Design
Zielgruppe
Ich bin Energieberater, habe mich vor kurzem selbstständig gemacht und möchte nun meine Bekanntheit steigern. Meine Zielgruppe sind Immobilieneigentümer sowie Immobiliensuchende, welchen ich eine fundierte Energieberatung mit Sanierungskonzepten sowie die Erstellung von Energieausweisen bieten kann.
Aufgabenstellung
Ich benötige einen Flyer, welchen ich regional verteilen möchte. Der Flyer soll quadratisch (148 x 148) erstellt werden.
Der Flyer sollte mein Logo, meine Kontaktdaten, die unten aufgeführten Dienstleistungen sowie einen Gutschein enthalten und insbesondere der Bekanntheits-/Imagesteigerung dienen.
Vorhandene Punkte sollen sein:
- Erstellung von Energieausweisen für Vermietung und Verkauf
- Energieberatung
- Sanierungs- und Modernisierungskonzepte
- Fördermittelberatung
Der Flyer soll die Möglichkeit bieten, am Rand abgeschnitten zu werden. Dort soll ein Gutschein aufgeführt werden mit 25 € Rabatt für einen Energieausweis.
Meine Kontaktdaten können Sie der angehängten Visitenkarte entnehmen.

```html
<!DOCTYPE html>
<html lang="de">
<head>
<meta charset="utf-8">
<title>Flyer Energieberatung – Gutschein</title>
<link rel="stylesheet" href="https://fonts.googleapis.com/css2?family=Arimo:wght@400;700&family=Libre+Baskerville:wght@700&display=swap">
<style>
  :root {
    --teal: #217d94;
    --red: #e1141c;
    --yellow: #f7ce12;
    --olive: #b4b51d;
    --ink: #111111;
    --night: #05070d;
    --paper: #ffffff;
    --board: #ffffff;
  }
  * { box-sizing: border-box; margin: 0; padding: 0; }
  html, body { width: 1200px; height: 1187px; overflow: hidden; background: var(--board); }
  body { position: relative; font-family: "Arimo", Arial, sans-serif; }

  .side-label {
    position: absolute; top: 166px; width: 351px; text-align: center;
    font-family: "Libre Baskerville", Georgia, serif; font-weight: 700;
    font-size: 22px; letter-spacing: 0.5px; color: var(--ink);
  }

  .card { position: absolute; overflow: hidden; }

  /* Front */
  .front { background: var(--night); }
  .front .photo {
    position: absolute; left: 0; top: 0; width: 100%;
    background:
      radial-gradient(ellipse 38% 34% at 48% 60%, #8a7a5e 0%, #3e4a4c 45%, rgba(10,14,20,0) 75%),
      radial-gradient(ellipse 70% 60% at 60% 55%, #1d2630 0%, var(--night) 80%);
  }
  .front .brand {
    position: absolute; display: flex; align-items: center; gap: 7px;
    color: var(--paper); font-weight: 700; text-transform: uppercase; letter-spacing: 1px;
  }
  .front .brand .mark { background: var(--teal); }
  .front .voucher-band {
    position: absolute; left: 0; bottom: 0; width: 100%;
    display: flex; align-items: center; justify-content: center;
    border-top: 1px dashed rgba(255,255,255,0.6);
    color: var(--paper); letter-spacing: 3px;
  }

  .front--main { left: 201px; top: 245px; width: 351px; height: 351px; }
  .front--main .photo { height: 266px; }
  .front--main .brand { left: 36px; top: 55px; font-size: 11px; }
  .front--main .brand .mark { width: 12px; height: 12px; }
  .front--main .voucher-band { height: 85px; font-size: 49px; background: var(--teal); }

  .front--small { top: 831px; width: 247px; height: 247px; }
  .front--small .photo { height: 187px; }
  .front--small .brand { left: 25px; top: 38px; font-size: 8px; gap: 5px; }
  .front--small .brand .mark { width: 9px; height: 9px; }
  .front--small .voucher-band { height: 60px; font-size: 35px; letter-spacing: 2px; }

  .front--yellow { left: 182px; }
  .front--yellow .voucher-band { background: var(--yellow); color: var(--ink); }
  .front--red { left: 471px; }
  .front--red .voucher-band { background: var(--red); }
  .front--olive { left: 761px; }
  .front--olive .voucher-band { background: var(--olive); color: var(--ink); }

  /* Back */
  .back { left: 640px; top: 245px; width: 351px; height: 351px; background: var(--paper); }
  .service {
    position: absolute; transform: rotate(-3deg); transform-origin: left center;
    display: flex; align-items: center; padding-left: 24px;
    font-size: 13px; line-height: 1.2; white-space: nowrap;
  }
  .service--certificates { left: 0; top: 38px; width: 293px; height: 52px; background: var(--teal); color: var(--paper); }
  .service--consulting { left: 51px; top: 84px; width: 176px; height: 27px; background: var(--red); color: var(--paper); font-weight: 700; }
  .service--funding { left: 75px; top: 109px; width: 216px; height: 27px; background: var(--yellow); color: var(--ink); font-weight: 700; padding-left: 20px; }
  .service--concepts { left: 24px; top: 138px; width: 340px; height: 31px; background: var(--olive); color: var(--ink); padding-left: 14px; }

  .contact-row { position: absolute; left: 0; top: 206px; width: 100%; height: 58px; }
  .contact-row .brand {
    position: absolute; left: 27px; top: 20px; display: flex; align-items: center; gap: 5px;
    color: var(--teal); font-size: 8px; font-weight: 700; letter-spacing: 0.8px; text-transform: uppercase;
  }
  .contact-row .brand .mark { width: 8px; height: 8px; background: var(--teal); }
  .contact-row .divider { position: absolute; left: 183px; top: 0; width: 2px; height: 58px; background: var(--teal); }
  .contact-row address {
    position: absolute; left: 195px; top: 7px; font-style: normal;
    font-size: 8px; line-height: 10.2px; color: var(--ink);
  }
  .offer {
    position: absolute; left: 0; bottom: 0; width: 100%; height: 85px; background: #000;
    border-top: 1px dashed rgba(255,255,255,0.5);
  }
  .offer .amount { position: absolute; left: 34px; top: 13px; font-size: 25px; font-weight: 700; color: var(--paper); }
  .offer .subject { position: absolute; left: 95px; top: 46px; font-size: 14.5px; color: var(--teal); }
</style>
</head>
<body>
  <h2 class="side-label" style="left:201px">Vorderseite</h2>
  <h2 class="side-label" style="left:640px">Rückseite</h2>

  <section class="card front front--main">
    <div class="photo" role="img" aria-label="Foto einer liegenden Glühbirne vor dunklem Hintergrund"></div>
    <div class="brand"><span class="mark"></span>Energieberatung Weller</div>
    <div class="voucher-band">GUTSCHEIN</div>
  </section>

  <section class="card back">
    <div class="service service--certificates">ERSTELLUNG VON ENERGIEAUSWEISEN<br>FÜR VERMIETUNG UND VERKAUF</div>
    <div class="service service--consulting">ENERGIEBERATUNG</div>
    <div class="service service--funding">FÖRDERMITTELBERATUNG</div>
    <div class="service service--concepts">SANIERUNGS- &amp; MODERNISIERUNGSKONZEPTE</div>
    <div class="contact-row">
      <div class="brand"><span class="mark"></span>Energieberatung Weller</div>
      <div class="divider"></div>
      <address>
        Am Lindenhof 4 | 35390 Gießen<br>
        +49 0151 47209316<br>
        info@energieberatung-weller.de<br>
        www.energieberatung-weller.de
      </address>
    </div>
    <div class="offer">
      <div class="amount">25 Euro Rabatt</div>
      <div class="subject">FÜR EINEN ENERGIEAUSWEIS</div>
    </div>
  </section>

  <section class="card front front--small front--yellow">
    <div class="photo" role="img" aria-label="Foto einer liegenden Glühbirne vor dunklem Hintergrund"></div>
    <div class="brand"><span class="mark"></span>Energieberatung Weller</div>
    <div class="voucher-band">GUTSCHEIN</div>
  </section>
  <section class="card front front--small front--red">
    <div class="photo" role="img" aria-label="Foto einer liegenden Glühbirne vor dunklem Hintergrund"></div>
    <div class="brand"><span class="mark"></span>Energieberatung Weller</div>
    <div class="voucher-band">GUTSCHEIN</div>
  </section>
  <section class="card front front--small front--olive">
    <div class="photo" role="img" aria-label="Foto einer liegenden Glühbirne vor dunklem Hintergrund"></div>
    <div class="brand"><span class="mark"></span>Energieberatung Weller</div>
    <div class="voucher-band">GUTSCHEIN</div>
  </section>
</body>
</html>
```